Layout für Broschüre für chemiefreie Lösung, Kühlwasser aufzubereiten
Zielgruppe
VELKORANIX hat eine Technologie entwickelt, die in der Industrie eingesetzt wird um in geschlossenen und offenen Kühlkreisläufen ohne Biozide und Korrosion Inhibitoren das Kühlwasser aufzubereiten. Mit VELKORANIX haben die Unternehmen eine chemiefreie Lösungen gegen Biofouling, Korrosion und Kalk. Zielgruppe sind alle Unternehmen die etwas produzieren oder Klimaanlagen / Heizungssysteme betreiben. Es geht um zukunftsorientierte und vor allem nachhaltige Technologie ohne Einsatz von Chemie.
Aufgabenstellung
Wir suchen für die Broschüre ein neues Layout, dass geradlinig und klar strukturiert ist, vor allem modern. Die Broschüre sollte DIN A 4 - Format sein in der gewohnten Struktur Umschlagseite innen und außen und 8 - 10 Innenseiten. Im Layout sollte ein roter Faden zu erkennen sein, aber nicht jede Seite gleich aussehen. Die Anlagen sind nur beispielhaft vom bestehenden Material und sollten vom Layout keinesfalls eine Orientierung geben, denn das soll verändert werden. Die Anlagen sind für einen inhaltlichen Überblick.

```html
<!DOCTYPE html>
<html lang="de">
<head>
<meta charset="utf-8">
<title>VELKORANIX – Broschüre Umschlag</title>
<link rel="stylesheet" href="https://fonts.googleapis.com/css2?family=Work+Sans:wght@300;400;600&display=swap">
<style>
  :root {
    --stage: #d2d2d2;
    --teal-deep: #0c4252;
    --teal-band: #4c8493;
    --photo-dark: #3a3a3a;
    --photo-mid: #7a7a7a;
    --photo-light: #b5b5b5;
    --white: #f4f4f2;
    --accent-green: #8cc63f;
    --text-soft: #6aa5b3;
  }
  * { margin: 0; padding: 0; box-sizing: border-box; }
  html, body {
    width: 1200px; height: 900px; overflow: hidden;
    background: var(--stage);
    font-family: "Work Sans", Arial, sans-serif;
  }
  .spread {
    position: absolute; left: 180px; top: 153px;
    width: 840px; height: 594px;
    display: flex;
    box-shadow: 0 12px 30px rgba(0,0,0,0.18);
  }
  .page { position: relative; width: 420px; height: 594px; overflow: hidden; }

  /* Back cover */
  .back-cover { background: var(--teal-deep); }
  .back-info {
    position: absolute; left: 44px; bottom: 70px; width: 260px;
  }
  .back-headline {
    font-size: 11px; font-weight: 400; color: var(--text-soft);
    margin-bottom: 6px;
  }
  .back-lines { font-size: 6.5px; line-height: 1.5; color: var(--text-soft); opacity: 0.8; }
  .brand {
    display: flex; align-items: center; gap: 5px;
    font-weight: 600; color: var(--white); letter-spacing: 0.04em;
  }
  .brand-dot { width: 9px; height: 9px; border-radius: 50%; background: var(--accent-green); }
  .back-info .brand { margin-top: 12px; font-size: 10px; }

  /* Front cover */
  .front-cover { background: var(--teal-band); }
  .cover-photo {
    position: absolute; left: 0; top: 0; width: 420px; height: 360px;
    background:
      radial-gradient(ellipse 45% 30% at 55% 35%, var(--photo-light), transparent 70%),
      radial-gradient(ellipse 70% 40% at 40% 85%, var(--photo-mid), transparent 75%),
      linear-gradient(180deg, #5a5a5a 0%, var(--photo-dark) 55%, #555 100%);
  }
  .cover-title {
    position: absolute; left: 40px; top: 282px;
    font-size: 27px; font-weight: 300; line-height: 1.08;
    color: var(--white); letter-spacing: 0.01em;
  }
  .title-swoosh { position: absolute; left: 38px; top: 340px; }
  .cover-subtitle {
    position: absolute; left: 42px; top: 410px;
    font-size: 10px; letter-spacing: 0.12em; color: var(--white);
  }
  .front-cover .brand { position: absolute; right: 36px; bottom: 48px; font-size: 10px; }
</style>
</head>
<body>
  <main class="spread">
    <section class="page back-cover">
      <div class="back-info">
        <p class="back-headline">Sauberes Kühlwasser ohne jede Chemie</p>
        <p class="back-lines">Nachhaltige Technologie für offene und geschlossene Kreisläufe<br>
          gegen Biofouling, Korrosion und Kalk in der Industrie<br>
          für Produktion, Klimaanlagen und Heizungssysteme</p>
        <div class="brand"><span class="brand-dot"></span>VELKORANIX</div>
      </div>
    </section>

    <section class="page front-cover">
      <div class="cover-photo" role="img" aria-label="Schwarzweißfoto: Hand in Wasser mit aufspritzenden Tropfen"></div>
      <h1 class="cover-title">CHEMIEFREIE<br>WASSERBEHANDLUNG</h1>
      <svg class="title-swoosh" width="200" height="20" viewBox="0 0 200 20" aria-hidden="true">
        <path d="M2 16 Q100 14 196 2" fill="none" stroke="var(--white)" stroke-width="2.5" stroke-linecap="round"/>
      </svg>
      <p class="cover-subtitle">LOREM IPSUM DOLORES</p>
      <div class="brand"><span class="brand-dot"></span>VELKORANIX</div>
    </section>
  </main>
</body>
</html>
```